I am writing a book called "SMILING OPENS EVERY DOOR "

I NEED A BOOK COVER FOR MY BOOK" SMILING OPENS EVERY DOOR"
so what was the question? " ( this in smaller font)

"Smiling Opens Every Door " will need to designed to eventually be a logo , banner and business card
COLOURS MAINLY ORANGE AND WHITE (with accents bright colour )

THE BOOK IS MY LAUGHTER JOURNEY AS A PERFORMER AND ADVENTURE INDIA LEARNING ABOUT LAUGHTER YOGA WHICH I WILL BE TEACHING

I do not want photos on the front cover ..
The look could be modern and eye-catching
I have also just been to India to learn Laughing Yoga with Dr Tobin Verhaal

Thank-you so much everyone for your brilliant designs . i am overwhelmed with your talent . i hope to work with you all again soon ! Marnie  

Target Market(s)

"Adults based in western speaking countries aged 25 to 60 that want to learn to laugh more
Also this book will be sold at my conference workshops

Industry/Entity Type

Business

Requirements
Must have
• ORANGE AND WHITE
CAN HAVE AQUA , HOT PINK , LIME GREEN, YELLOW ACCENTS

THESE WILL BE DIFFERENT AREAS WILL COVERING IN MY BOOK
EG LAUGHTER NAD BREAT CANCER ( PINK)
LAUGHTER NAD DEPRESSION ( BLUE)
LAUGHTER AND KIDS ( YELLOW)

NO Photos on front cover
Should not have
• No photos

```html
<!DOCTYPE html>
<html lang="en">
<head>
<meta charset="utf-8">
<title>Smiling Opens Every Door</title>
<link rel="stylesheet" href="https://fonts.googleapis.com/css2?family=Sniglet:wght@800&family=Montserrat:wght@500&family=Yellowtail&display=swap">
<style>
  :root {
    --orange: #ff7f27;
    --white: #ffffff;
    --lime: #b5e61d;
    --aqua: #99d9ea;
    --yellow: #fff200;
    --pink: #ff8ec6;
    --grey: #7f7f7f;
    --red: #ed1c24;
  }
  html, body {
    margin: 0;
    padding: 0;
    overflow: hidden;
    background: var(--orange);
  }
  .cover {
    display: block;
    width: 1200px;
    height: 1000px;
    background: var(--orange);
  }
  .title-main {
    font-family: "Sniglet", "Comic Sans MS", sans-serif;
    font-weight: 800;
    font-size: 220px;
    fill: var(--white);
  }
  .title-sub {
    font-family: "Montserrat", Arial, sans-serif;
    font-weight: 500;
    font-size: 72px;
    fill: var(--grey);
  }
  .tagline {
    font-family: "Yellowtail", cursive;
    font-size: 62px;
    fill: var(--lime);
  }
</style>
</head>
<body>
<svg class="cover" viewBox="0 0 1200 1000" xmlns="http://www.w3.org/2000/svg">
  <defs>
    <linearGradient id="flourish-tones" x1="0" x2="1" y1="0" y2="0">
      <stop offset="0" stop-color="var(--aqua)"/>
      <stop offset="0.33" stop-color="var(--aqua)"/>
      <stop offset="0.34" stop-color="var(--yellow)"/>
      <stop offset="0.66" stop-color="var(--yellow)"/>
      <stop offset="0.67" stop-color="var(--pink)"/>
      <stop offset="1" stop-color="var(--pink)"/>
    </linearGradient>
  </defs>

  <!-- accent blocks -->
  <rect class="accent-lime" x="987" y="35" width="206" height="160" fill="var(--lime)"/>
  <rect class="accent-lime-window" x="988" y="113" width="157" height="81" fill="var(--orange)" stroke="var(--lime)" stroke-width="2"/>
  <rect class="accent-aqua" x="6" y="606" width="208" height="154" fill="var(--aqua)"/>
  <rect class="accent-aqua-window" x="24" y="607" width="189" height="75" fill="var(--orange)" stroke="var(--aqua)" stroke-width="2"/>

  <!-- frame -->
  <rect class="frame" x="24" y="113" width="1121" height="569" fill="none" stroke="var(--white)" stroke-width="2"/>

  <!-- title -->
  <text class="title-main" x="45" y="400" textLength="1070" lengthAdjust="spacingAndGlyphs">SMILING</text>
  <text class="title-sub" x="160" y="362" textLength="835" lengthAdjust="spacing">OPENS EVERY DOOR</text>
  <path class="smile" d="M322 372 Q362 398 404 374" fill="none" stroke="var(--red)" stroke-width="7" stroke-linecap="round"/>

  <!-- tagline -->
  <text class="tagline" x="567" y="482" text-anchor="middle">- so what was the question? -</text>

  <!-- flourish divider -->
  <rect class="flourish" role="img" aria-label="Three curled flourish ornaments in aqua, yellow and pink" x="400" y="520" width="290" height="32" rx="16" fill="url(#flourish-tones)"/>
</svg>
</body>
</html>
```